Marketing Brochure For Tallbrook LLC for marketing and advertising purposes.A slick and modern design. I have added in the attachment a PDF called Tallbrook Profile which is the old version of this new one we are creating but can give you an idea of what I am looking for. I also have a Word document called New Consulting Document that lists each topic, where the attached images go, and the wording that goes in each. The total brochure should be between 8 and 12 pages.

Industry/Entity Type

Credit Card

Font styles to use
Serif

Colors
f78f20
886aae

Requirements
Must have
• A slick and modern design. I have added in the attachment a PDF called Tallbrook Profile which is the old version of this new one we are creating but can give you an idea of what I am looking for. I also have a Word document called New Consulting Document that lists each topic, where the attached images go, and the wording that goes in each. The total brochure should be between 8 and 12 pages.

```html
<!DOCTYPE html>
<html lang="en">
<head>
<meta charset="utf-8">
<title>Tallbrook LLC – Brochure Spreads</title>
<link href="https://fonts.googleapis.com/css2?family=Open+Sans:wght@400;600;700&family=Arimo:wght@700&display=swap" rel="stylesheet">
<style>
  :root{
    --orange:#f78f20;
    --purple:#886aae;
    --purple-deep:#7a5a9e;
    --rose:#c27ca6;
    --tab:#3b3b3d;
    --ink:#3c3c3c;
    --soft:#6a6a6a;
    --paper:#ffffff;
    --stage:#e9e7e4;
  }
  *{box-sizing:border-box;margin:0;padding:0}
  html,body{width:1200px;height:1200px;overflow:hidden;background:var(--stage)}
  body{position:relative;font-family:"Open Sans",Arial,sans-serif;color:var(--ink)}
  .page{position:absolute;width:350px;height:494px;background:var(--paper);overflow:hidden;box-shadow:0 6px 18px rgba(0,0,0,.18)}
  .page--front{left:68px;top:90px}
  .page--back{left:758px;top:90px}
  .page--inside-1{left:68px;top:677px}
  .page--inside-2{left:758px;top:677px}
  .abs{position:absolute}
  .mountain{position:absolute;left:0;right:0;bottom:0;background:linear-gradient(180deg,rgba(255,255,255,0) 0%,#e3e3e3 35%,#d6d6d6 60%,#ececec 100%)}
  .footer-bar{position:absolute;left:0;right:0;bottom:0;height:18px;background:var(--orange)}
  .footer-tab{position:absolute;bottom:10px;left:50%;transform:translateX(-50%);width:152px;height:22px;background:var(--tab);clip-path:polygon(0 0,100% 0,93% 100%,7% 100%);color:#fff;font-weight:600;font-size:9.6px;text-align:center;line-height:22px}
  /* front */
  .cover-photo{left:0;top:0;width:350px;height:304px;background:linear-gradient(160deg,#bcd7ef 0%,#3f7fc4 30%,#163f85 60%,#0b1f4d 100%)}
  .tagline{left:0;top:329px;width:160px;height:116px;background:var(--rose);color:#fff;font-family:"Arimo",Arial,sans-serif;font-weight:700;font-size:19px;line-height:25px;padding:20px 0 0 16px}
  .brand{font-family:"Open Sans",Arial,sans-serif;font-weight:600;color:var(--purple);display:flex;align-items:center;gap:8px}
  .brand-dot{width:14px;height:14px;border-radius:50%;background:var(--orange)}
  .brand--front{left:188px;top:378px;font-size:24px}
  /* back */
  .brand--back{left:0;right:0;top:150px;justify-content:center;font-size:32px}
  .contact{left:0;right:0;top:193px;text-align:center;font-size:10.5px;color:var(--ink);line-height:1.2}
  .contact svg{display:block;margin:0 auto 2px}
  .contact .row{margin-bottom:5px}
  /* inside */
  .band{position:absolute;left:0;height:12px;background:var(--purple);color:#fff;font-weight:700;font-size:9.4px;line-height:12px;padding-left:12px;letter-spacing:.2px}
  .band::after{content:"";position:absolute;top:0;right:-30px;width:30px;height:12px;background:repeating-linear-gradient(60deg,var(--purple) 0 2px,transparent 2px 4px)}
  .copy{position:absolute;font-size:5.7px;line-height:8.4px;color:var(--soft);text-align:justify}
  .copy p+p{margin-top:8px}
  .art{position:absolute;border:1px solid #c8a6c6}
  .subhead{position:absolute;left:12px;right:12px;font-weight:700;font-size:7.4px;color:#222;display:flex;align-items:center;gap:5px}
  .subhead::after{content:"";flex:1;height:1px;background:#8a8a8a}
  .bullets{position:absolute;list-style:none;font-size:5.7px;line-height:8.4px;color:var(--soft);text-align:justify}
  .bullets li{position:relative;padding-left:11px}
  .bullets li+li{margin-top:7px}
  .bullets li::before{content:"";position:absolute;left:1px;top:2px;width:4px;height:4px;border:1px solid var(--purple);border-radius:50%}
</style>
</head>
<body>

<!-- FRONT COVER -->
<section class="page page--front">
  <div class="abs cover-photo" role="img" aria-label="Photo looking up at glass skyscrapers against a blue sky"></div>
  <div class="mountain" style="top:330px" role="img" aria-label="Faint misty mountain range"></div>
  <div class="abs tagline">ENGAGE,<br>INSPIRE<br>&amp; EMPOWER</div>
  <div class="abs brand brand--front"><span class="brand-dot"></span>Tallbrook</div>
  <div class="footer-bar"></div>
  <div class="footer-tab">www.tallbrookconsult.com</div>
</section>

<!-- BACK COVER -->
<section class="page page--back">
  <div class="mountain" style="top:280px" role="img" aria-label="Faint misty mountain range"></div>
  <div class="abs brand brand--back"><span class="brand-dot" style="width:18px;height:18px"></span>Tallbrook</div>
  <div class="abs contact">
    <div class="row">
      <svg width="12" height="11" viewBox="0 0 24 22"><path fill="#886aae" d="M2 8c0-4 20-4 20 0l-4 3-3-2V7H9v2l-3 2zM5 12h14l2 9H3z"/><circle cx="12" cy="16" r="2.5" fill="#fff"/></svg>
      (555) 014-2207
    </div>
    <div class="row">
      <svg width="12" height="12" viewBox="0 0 24 24"><circle cx="12" cy="12" r="10" fill="#886aae"/><path d="M2 12h20M12 2c4 4 4 16 0 20M12 2c-4 4-4 16 0 20" stroke="#fff" stroke-width="1.5" fill="none"/></svg>
      www.tallbrookconsult.com
    </div>
    <div class="row">
      <svg width="13" height="10" viewBox="0 0 26 20"><rect width="26" height="20" rx="2" fill="#886aae"/><path d="M1 2l12 9 12-9" stroke="#fff" stroke-width="1.8" fill="none"/></svg>
      dana.reeve@tallbrookconsult.com
    </div>
  </div>
</section>

<!-- INSIDE 1 -->
<section class="page page--inside-1">
  <div class="mountain" style="top:250px" role="img" aria-label="Faint misty mountain range"></div>
  <div class="band" style="top:14px;width:104px">CONSULTING</div>
  <div class="abs" style="left:14px;top:62px;width:160px;height:56px;background:linear-gradient(90deg,#f4f1ee,#e9e4ef)" role="img" aria-label="Consulting illustration with small icons for goal, expert, knowledge, strategy, advice, support and success"></div>
  <div class="copy" style="left:187px;top:28px;width:152px">
    <p>Tallbrook LLC provides consulting services and specializes in the credit and collection industry. The area of focus for consulting is debt collection agencies, creditors, asset buyers, and solution providers. Our consulting services are focused on two avenues; staying ahead of the curve and turning challenging situations into positive experiences.</p>
    <p>Tallbrook offers a holistic approach to it's consulting but also offers an ala carte process by focusing in the areas of Operational Excellence, Compliance, Employee Development, Business Development, Client Experience, Information Technology, and Public Relations. Tallbrook takes great pride in getting organizations to obtain maximum output with minimum input while increasing efficiency, effectiveness, and profitability.</p>
  </div>
  <div class="band" style="top:168px;width:142px">LEADERSHIP COACHING</div>
  <div class="copy" style="left:12px;top:193px;width:153px">
    <p>Tallbrook also specializes in leadership coaching with a focus on mid-level, senior, and executive level management. We have found over the years that most organizations do a good enough job in training their front line employees but fail to train the leaders that are leading the organization. That is where Tallbrook comes in, with over two decades of training all levels of employees our training program is customized to reach upper level</p>
  </div>
  <div class="abs" style="left:186px;top:218px;width:152px;height:34px;background:linear-gradient(90deg,#e8eef6,#eef6e6)" role="img" aria-label="Leadership coaching banner graphic with coloured circles"></div>
  <div class="abs" style="left:14px;top:292px;width:156px;height:150px;background:radial-gradient(circle at 50% 55%,#f6c39a 0%,#f3d7e4 45%,rgba(255,255,255,0) 75%)" role="img" aria-label="Diagram of arrows radiating to mindset, purpose, caring, communication and courage"></div>
  <div class="copy" style="left:187px;top:318px;width:152px">
    <p>We focus on where the individual or the organization wants or needs to be in order to be the most productive individually and corporately. Our program interacts with everyone on their level in a way that energizes them to achieve extraordinary results with desired objectives and goals in mind. It is important for us to identify and understand each situation and priorities of the individual and organization so that each unique situation is strategized on how to reach them while providing a learning environment that teaches them to overcome obstacles that rise along the journey. Tallbrook Leadership focus on five avenues; Mindset, Pur-</p>
  </div>
  <div class="footer-bar"></div>
  <div class="footer-tab">www.tallbrookconsult.com</div>
</section>

<!-- INSIDE 2 -->
<section class="page page--inside-2">
  <div class="mountain" style="top:280px" role="img" aria-label="Faint misty mountain range"></div>
  <div class="band" style="top:14px;width:130px">SERVICES PROVIDED</div>
  <div class="subhead" style="top:33px">OPERATIONAL EXCELLENCE</div>
  <ul class="bullets" style="left:12px;top:52px;width:151px">
    <li>We will provide an exhaustive and unbiased review of your organizations current collection strategies from a cradle to grave work flow standpoint. This will include best practices from across the industry and provide you with templated procedures, necessary reporting, workforce management, and ensuring your organization is working with the right technology providers at the right cost to the organization.</li>
    <li>We will also provide you with in-depth expert advice encompassing two decades of experience providing actionable solutions that will provide organizations with methods to increase recoveries, liquidation, and revenue.</li>
  </ul>
  <div class="art" style="left:187px;top:59px;width:150px;height:106px;background:linear-gradient(135deg,#f2f2f2,#e2e6ee)" role="img" aria-label="Sketched strategy development chart with pie chart and icons"></div>
  <ul class="bullets" style="left:12px;top:185px;width:326px">
    <li>If warranted, a full and complete review of the organizations profit, and loss statement would be reviewed and findings shared with executive management to identify areas and trends where the strengths and areas of opportunities lie.</li>
  </ul>
  <div class="subhead" style="top:232px">COMPLIANCE</div>
  <ul class="bullets" style="left:190px;top:253px;width:148px">
    <li>Perform an exhaustive review and determine the maturity of your organizations existing Compliance Management System</li>
    <li>Produce a framework to build upon a CMS from the current maturity level which includes development and/or enhancement of policies, procedures, controls, work instructions, exception reporting, and technology usage/opportu-</li>
    <li>Having gone through several Collections Guild Practice Standards System Certifications (CGPS) as an agency owner and certified instructor we are prepared to assist your organization to fast track this critical component of an agency's compliance management system. We can save you time, money, and resources by assisting with the awesome program.</li>
  </ul>
  <div class="art" style="left:12px;top:269px;width:151px;height:115px;background:linear-gradient(135deg,#f4f4f4,#e6e6e6)" role="img" aria-label="Compliance diagram surrounded by icons for rules, standards, governance, regulations, policies and law"></div>
  <ul class="bullets" style="left:12px;top:415px;width:326px">
    <li>If you are interested in learning how to implement processes that will streamline the state licensing and bonding, we can save you time, effort, and energy by showing you how to do it yourself or how to negotiate with the vendors available to assist you.</li>
  </ul>
  <div class="footer-bar"></div>
  <div class="footer-tab">www.tallbrookconsult.com</div>
</section>

</body>
</html>
```